Stainless Steel Business Card

I have a fiber laser and want to highlight its capabilities in a business card. On the card I want

Brisler Systems
Martin Pelko
martin@mpelkoworks.com
417-555-0136

This will be cut / engraved on stainless steel. I want the Brisler Systems to be prominent with laser cut font so that there are no dropouts on the O and A's. My name email and phone number should be engraved black. I would like some cool geometric patterns to cutout on the card to highlight the capabilities of my machine. I will need to files in the end either SVG or dxf of the engrave portion and the cut portion.

```html
<!DOCTYPE html>
<html lang="en">
<head>
<meta charset="utf-8">
<title>Brisler Systems – Business Card</title>
<link rel="stylesheet" href="https://fonts.googleapis.com/css2?family=Saira+Stencil+One&family=Orbitron:wght@700&display=swap">
<style>
  :root {
    --page-bg: #ffffff;
    --card-bg: #ffffff;
    --card-edge: #111111;
    --ink: #0b0b0b;
  }
  html, body {
    margin: 0;
    padding: 0;
    width: 1200px;
    height: 1001px;
    overflow: hidden;
    background: var(--page-bg);
  }
  .canvas {
    position: relative;
    width: 1200px;
    height: 1001px;
  }
  .business-card {
    position: absolute;
    left: 222px;
    top: 287px;
    width: 755px;
    height: 426px;
    box-sizing: border-box;
    border: 1.5px solid var(--card-edge);
    border-radius: 26px;
    background: var(--card-bg);
    color: var(--ink);
    text-align: center;
  }
  .brand-name {
    margin: 0;
    font-weight: 400;
    font-family: "Saira Stencil One", sans-serif;
  }
  .brand-name span {
    position: absolute;
    left: 0;
    right: 0;
    line-height: 1;
    white-space: nowrap;
  }
  .brand-primary {
    top: 48px;
    font-size: 98px;
    letter-spacing: 8px;
    padding-left: 8px;
  }
  .brand-secondary {
    top: 165px;
    font-size: 60px;
    letter-spacing: 12px;
    padding-left: 12px;
  }
  .contact {
    position: absolute;
    left: 0;
    right: 0;
    top: 283px;
    margin: 0;
    font-family: "Orbitron", sans-serif;
    font-weight: 700;
    font-style: normal;
    font-size: 17px;
    line-height: 29.5px;
    letter-spacing: 2px;
    text-transform: uppercase;
  }
  .contact span { display: block; white-space: nowrap; }
</style>
</head>
<body>
  <main class="canvas">
    <section class="business-card" aria-label="Brisler Systems business card">
      <h1 class="brand-name">
        <span class="brand-primary">BRISLER</span>
        <span class="brand-secondary">SYSTEMS</span>
      </h1>
      <address class="contact">
        <span class="contact-name">Martin Pelko</span>
        <span class="contact-email">martin@mpelkoworks.com</span>
        <span class="contact-phone">417·555·0136</span>
      </address>
    </section>
  </main>
</body>
</html>
```